Create a new business card

I’m looking to update my business card to make it match the rest of my brand. I will include my current website as well as what my vehicle designs look like, etc..
What my business currently services
Weekly maintenance pool openings / closings
Equipment repair, including pumps, heaters, salt systems, filters, etc.
We install automatic covers and maintain them as well as provide preventative maintenance

I would like to include my name.
Darren Holcott.
My title
Owner
My email
Darren@tidewellnx.com
4015867120
Www.tidewellnx.com

```html
<!DOCTYPE html>
<html lang="en">
<head>
<meta charset="utf-8">
<title>Tidewell Pool Care – Business Card</title>
<link rel="stylesheet" href="https://fonts.googleapis.com/css2?family=Poppins:wght@400;700&family=Roboto:ital,wght@0,400;1,700&display=swap">
<style>
  :root {
    --navy: #1f346b;
    --navy-deep: #1e3264;
    --orange: #f39c1f;
    --orange-text: #e8731f;
    --sky: #29abe2;
    --sky-soft: #bfe6f6;
    --ocean-top: #2b6a99;
    --ocean-bottom: #2a7fb0;
    --white: #ffffff;
    --page: #e8e8e8;
  }
  html, body {
    margin: 0;
    width: 1200px;
    height: 1200px;
    overflow: hidden;
    background: var(--page);
  }
  .card {
    position: absolute;
    left: 239px;
    width: 722px;
    height: 412px;
    border-radius: 17px;
    overflow: hidden;
    box-shadow: 0 6px 18px rgba(0,0,0,0.18);
  }
  .card--front { top: 140px; background: var(--white); }
  .card--back {
    top: 645px;
    background: linear-gradient(180deg, var(--ocean-top), var(--ocean-bottom));
  }
  .card__waves {
    position: absolute;
    inset: 0;
    width: 722px;
    height: 412px;
  }

  /* brand name block */
  .brand {
    position: absolute;
    display: flex;
    flex-direction: column;
    align-items: center;
    text-align: center;
    font-family: "Poppins", sans-serif;
    font-weight: 700;
    color: var(--navy);
  }
  .brand__dot {
    width: 46px;
    height: 46px;
    border-radius: 50%;
    background: var(--sky);
    margin-bottom: 12px;
  }
  .brand__name { font-size: 30px; line-height: 1.1; }
  .card--front .brand { left: 80px; top: 108px; width: 200px; }

  .divider {
    position: absolute;
    left: 337px;
    top: 79px;
    width: 3px;
    height: 194px;
    background: var(--sky);
  }

  .person {
    position: absolute;
    left: 390px;
    top: 72px;
    font-family: "Poppins", sans-serif;
  }
  .person__name {
    margin: 0;
    font-size: 29px;
    font-weight: 700;
    letter-spacing: 0.3px;
    color: var(--navy);
    line-height: 1.1;
  }
  .person__title {
    margin: 0;
    font-size: 24px;
    font-weight: 400;
    color: var(--orange-text);
    line-height: 1.1;
  }

  .contacts {
    position: absolute;
    left: 390px;
    top: 172px;
    margin: 0;
    padding: 0;
    list-style: none;
    font-family: "Roboto", sans-serif;
    font-size: 19px;
    color: var(--navy);
    letter-spacing: 0.4px;
  }
  .contacts__item {
    display: flex;
    align-items: center;
    height: 25px;
    margin-bottom: 13px;
  }
  .contacts__icon {
    width: 24px;
    height: 24px;
    margin-right: 13px;
    flex: none;
  }

  /* back */
  .splash {
    position: absolute;
    left: 222px;
    top: 40px;
    width: 290px;
    height: 255px;
    border-radius: 46% 54% 50% 50% / 52% 48% 52% 48%;
    background: radial-gradient(circle, var(--white) 62%, var(--sky-soft) 100%);
  }
  .card--back .brand { left: 246px; top: 96px; width: 240px; }
  .card--back .brand__name { font-size: 34px; }

  .tagline {
    position: absolute;
    left: 0;
    right: 0;
    top: 319px;
    margin: 0;
    text-align: center;
    font-family: "Roboto", sans-serif;
    font-style: italic;
    font-weight: 700;
    font-size: 17px;
    line-height: 23px;
    letter-spacing: 0.4px;
    color: var(--white);
    text-transform: uppercase;
  }
</style>
</head>
<body>

<section class="card card--front">
  <div class="brand">
    <span class="brand__dot"></span>
    <span class="brand__name">Tidewell<br>Pool Care</span>
  </div>

  <div class="divider"></div>

  <div class="person">
    <h1 class="person__name">DARREN HOLCOTT</h1>
    <p class="person__title">Owner</p>
  </div>

  <ul class="contacts">
    <li class="contacts__item">
      <svg class="contacts__icon" viewBox="0 0 24 24" aria-hidden="true">
        <circle cx="12" cy="12" r="12" fill="#1f346b"/>
        <path d="M8.4 6.5l1.8-.4 1.2 2.8-1.3 1c.6 1.4 1.6 2.4 3 3l1-1.3 2.8 1.2-.4 1.8c-.2.6-.7 1-1.3.9-3.8-.4-6.8-3.4-7.2-7.2 0-.6.3-1.1.9-1.3z" fill="#fff"/>
      </svg>
      40 1586 7120
    </li>
    <li class="contacts__item">
      <svg class="contacts__icon" viewBox="0 0 24 24" aria-hidden="true">
        <circle cx="12" cy="12" r="12" fill="#1f346b"/>
        <rect x="6.5" y="8" width="11" height="8" rx="1" fill="#fff"/>
        <path d="M7 8.6l5 3.8 5-3.8" fill="none" stroke="#1f346b" stroke-width="1.2"/>
      </svg>
      Darren@tidewellnx.com
    </li>
    <li class="contacts__item">
      <svg class="contacts__icon" viewBox="0 0 24 24" aria-hidden="true">
        <circle cx="12" cy="12" r="11" fill="none" stroke="#1f346b" stroke-width="2"/>
        <ellipse cx="12" cy="12" rx="4.5" ry="11" fill="none" stroke="#1f346b" stroke-width="2"/>
        <path d="M1 12h22M3 6.5h18M3 17.5h18" stroke="#1f346b" stroke-width="2"/>
      </svg>
      www.tidewellnx.com
    </li>
  </ul>

  <svg class="card__waves" viewBox="0 0 722 412" aria-hidden="true">
    <path class="wave wave--orange" d="M0 328 C110 322 200 364 307 363 C380 362 430 336 520 331 C620 326 700 318 722 302 L722 412 L0 412 Z" fill="var(--orange)"/>
    <path class="wave wave--navy" d="M0 360 C100 372 220 378 307 372 C400 366 450 352 520 349 C620 345 700 330 722 306 L722 412 L0 412 Z" fill="var(--navy-deep)"/>
    <path class="wave wave--swoosh" d="M279 394 C300 378 330 366 372 358 L380 362 C338 370 306 381 279 394 Z" fill="var(--orange)"/>
  </svg>
</section>

<section class="card card--back">
  <svg class="card__waves" viewBox="0 0 722 412" aria-hidden="true">
    <path d="M0 300 Q361 130 722 300 L722 412 L0 412 Z" fill="var(--orange)"/>
    <path d="M0 318 Q361 168 722 318 L722 412 L0 412 Z" fill="var(--navy-deep)"/>
  </svg>

  <div class="splash" role="img" aria-label="White paint splash with light blue droplets behind the brand name"></div>

  <div class="brand">
    <span class="brand__dot"></span>
    <span class="brand__name">Tidewell<br>Pool Care</span>
  </div>

  <p class="tagline">Specializing in gunite pools<br>Weekly service</p>
</section>

</body>
</html>
```